Schmuckzertifikat im Visitenkarten-Format für Gold und Silberschmuck (Echtschmuck)
Zielgruppe
Echtschmuckverkauf im Internet / Gold und Silber in verschiedenen Legierungen
Aufgabenstellung
Wir benötigen ein Schmuckzertifikat in Visitenkartengröße
Die Karte sollte beidseitig bedruckt sein, einen seriösen und sehr edlen Eindruck machen.
Das Zertifikat wird für Silber-und Goldschmuck genutzt.
Eine Kartendesign für Goldschmuck und ein Kartendesign für Silberschmuck ist gewünscht.
Unterschied ist dann nur die Farbe Gold/Silber bei gleichbleibendem Design.
Das Zertifikat wird entweder einem Goldschmuck oder einem Silberschmuck-Artikel beigelegt und sollte deswegen farblich etwas zum Schmuck passen, Gold/Silber.
Enthaltene Wörter können sein:
'Echtheitsgarantie' und 'Premium-Qualität Made in Germany' 'Schmuckzertifikat'
'Garantie der Punzierung (Stempel)'
Für die
'Der Gold-Feingehalt, Punzierung (Stempel) auf dem Schmuckstück, wird hiermit garantiert'
'Der Silber-Feingehalt, Punzierung (Stempel) auf dem Schmuckstück, wird hiermit garantiert'
Der Text kann auch nach Ihren Vorstellungen abweichen.
Das Zertifikat soll ein Siegel enthalten und universell auf Gold- und Silberschmuck passen.
Die Marke 'SOLTARIN' sollte auf der Karte deutlich erkennbar sein.

```html
<!DOCTYPE html>
<html lang="de">
<head>
<meta charset="utf-8">
<title>SOLTARIN Schmuckzertifikat</title>
<link rel="stylesheet" href="https://fonts.googleapis.com/css2?family=Tinos&display=swap">
<style>
  :root {
    --paper: #ffffff;
    --navy: #10101f;
    --silver-light: #c4c4c4;
    --silver-dark: #cfcfd3;
    --gold: #c39a2c;
    --gold-dark: #c79f32;
    --edge: #cfcfcf;
  }
  html, body {
    margin: 0;
    width: 1200px;
    height: 1200px;
    overflow: hidden;
    background: #ffffff;
    font-family: "Tinos", "Times New Roman", serif;
  }
  .sheet {
    width: 1200px;
    height: 1200px;
    box-sizing: border-box;
    padding: 20px 100px;
    display: grid;
    grid-template-columns: 480px 480px;
    grid-template-rows: repeat(4, 275px);
    column-gap: 40px;
    row-gap: 20px;
  }
  .card {
    width: 480px;
    height: 275px;
    box-sizing: border-box;
    display: block;
  }
  .card svg { display: block; width: 100%; height: 100%; }
  .card--light { background: var(--paper); border: 1px solid var(--edge); }
  .card--dark { background: var(--navy); }
  .card--silver.card--light { color: var(--silver-light); }
  .card--silver.card--dark { color: var(--silver-dark); }
  .card--gold.card--light { color: var(--gold); }
  .card--gold.card--dark { color: var(--gold-dark); }
  .brand { font-size: 40px; letter-spacing: 1px; }
  .seal-arc-text { font-size: 11px; letter-spacing: 1px; }
  .seal-center { font-size: 19px; }
  .guarantee { font-size: 22px; }
</style>
</head>
<body>
<main class="sheet">

  <!-- Silver on white: front -->
  <section class="card card--light card--silver" aria-label="Vorderseite Silber hell">
    <svg viewBox="0 0 443 254" fill="currentColor">
      <text class="brand" transform="translate(133 127) rotate(-90)" text-anchor="middle" dominant-baseline="middle">SOLTARIN</text>
      <g class="seal" transform="rotate(-90 320 128)">
        <circle cx="320" cy="128" r="87" fill="none" stroke="currentColor" stroke-width="6"/>
        <circle cx="320" cy="128" r="69" fill="none" stroke="currentColor" stroke-width="1.5"/>
        <path id="arc-1" d="M 242 128 A 78 78 0 0 1 398 128" fill="none"/>
        <text class="seal-arc-text"><textPath href="#arc-1" startOffset="50%" text-anchor="middle" dominant-baseline="middle">PREMIUM-QUALITÄT</textPath></text>
        <text class="seal-center" x="320" y="108" text-anchor="middle">MADE</text>
        <text class="seal-center" x="320" y="132" text-anchor="middle">IN</text>
        <text class="seal-center" x="320" y="156" text-anchor="middle">GERMANY</text>
      </g>
    </svg>
  </section>

  <!-- Silver on white: back -->
  <section class="card card--light card--silver" aria-label="Rückseite Silber hell">
    <svg viewBox="0 0 443 254" fill="currentColor">
      <rect x="57" y="50" width="338" height="148" fill="none" stroke="currentColor" stroke-width="2"/>
      <rect x="63" y="56" width="326" height="136" fill="none" stroke="currentColor" stroke-width="3"/>
      <text class="guarantee" text-anchor="middle">
        <tspan x="226" y="86">Der Silber-Feingehalt,</tspan>
        <tspan x="226" y="115">Punzierung (Stempel) auf</tspan>
        <tspan x="226" y="144">dem Schmuckstück, wird</tspan>
        <tspan x="226" y="173">hiermit garantiert</tspan>
      </text>
    </svg>
  </section>

  <!-- Silver on navy: front -->
  <section class="card card--dark card--silver" aria-label="Vorderseite Silber dunkel">
    <svg viewBox="0 0 443 254" fill="currentColor">
      <text class="brand" transform="translate(133 127) rotate(-90)" text-anchor="middle" dominant-baseline="middle">SOLTARIN</text>
      <g class="seal" transform="rotate(-90 320 128)">
        <circle cx="320" cy="128" r="87" fill="none" stroke="currentColor" stroke-width="6"/>
        <circle cx="320" cy="128" r="69" fill="none" stroke="currentColor" stroke-width="1.5"/>
        <path id="arc-2" d="M 242 128 A 78 78 0 0 1 398 128" fill="none"/>
        <text class="seal-arc-text"><textPath href="#arc-2" startOffset="50%" text-anchor="middle" dominant-baseline="middle">PREMIUM-QUALITÄT</textPath></text>
        <text class="seal-center" x="320" y="108" text-anchor="middle">MADE</text>
        <text class="seal-center" x="320" y="132" text-anchor="middle">IN</text>
        <text class="seal-center" x="320" y="156" text-anchor="middle">GERMANY</text>
      </g>
    </svg>
  </section>

  <!-- Silver on navy: back -->
  <section class="card card--dark card--silver" aria-label="Rückseite Silber dunkel">
    <svg viewBox="0 0 443 254" fill="currentColor">
      <rect x="57" y="50" width="338" height="148" fill="none" stroke="currentColor" stroke-width="2"/>
      <rect x="63" y="56" width="326" height="136" fill="none" stroke="currentColor" stroke-width="3"/>
      <text class="guarantee" text-anchor="middle">
        <tspan x="226" y="86">Der Silber-Feingehalt,</tspan>
        <tspan x="226" y="115">Punzierung (Stempel) auf</tspan>
        <tspan x="226" y="144">dem Schmuckstück, wird</tspan>
        <tspan x="226" y="173">hiermit garantiert</tspan>
      </text>
    </svg>
  </section>

  <!-- Gold on white: front -->
  <section class="card card--light card--gold" aria-label="Vorderseite Gold hell">
    <svg viewBox="0 0 443 254" fill="currentColor">
      <text class="brand" transform="translate(133 127) rotate(-90)" text-anchor="middle" dominant-baseline="middle">SOLTARIN</text>
      <g class="seal" transform="rotate(-90 320 128)">
        <circle cx="320" cy="128" r="87" fill="none" stroke="currentColor" stroke-width="6"/>
        <circle cx="320" cy="128" r="69" fill="none" stroke="currentColor" stroke-width="1.5"/>
        <path id="arc-3" d="M 242 128 A 78 78 0 0 1 398 128" fill="none"/>
        <text class="seal-arc-text"><textPath href="#arc-3" startOffset="50%" text-anchor="middle" dominant-baseline="middle">PREMIUM-QUALITÄT</textPath></text>
        <text class="seal-center" x="320" y="108" text-anchor="middle">MADE</text>
        <text class="seal-center" x="320" y="132" text-anchor="middle">IN</text>
        <text class="seal-center" x="320" y="156" text-anchor="middle">GERMANY</text>
      </g>
    </svg>
  </section>

  <!-- Gold on white: back -->
  <section class="card card--light card--gold" aria-label="Rückseite Gold hell">
    <svg viewBox="0 0 443 254" fill="currentColor">
      <rect x="50" y="50" width="338" height="148" fill="none" stroke="currentColor" stroke-width="2"/>
      <rect x="56" y="56" width="326" height="136" fill="none" stroke="currentColor" stroke-width="3"/>
      <text class="guarantee" text-anchor="middle">
        <tspan x="219" y="86">Der Gold-Feingehalt,</tspan>
        <tspan x="219" y="115">Punzierung (Stempel) auf</tspan>
        <tspan x="219" y="144">dem Schmuckstück, wird</tspan>
        <tspan x="219" y="173">hiermit garantiert</tspan>
      </text>
    </svg>
  </section>

  <!-- Gold on navy: front -->
  <section class="card card--dark card--gold" aria-label="Vorderseite Gold dunkel">
    <svg viewBox="0 0 443 254" fill="currentColor">
      <text class="brand" transform="translate(133 127) rotate(-90)" text-anchor="middle" dominant-baseline="middle">SOLTARIN</text>
      <g class="seal" transform="rotate(-90 320 128)">
        <circle cx="320" cy="128" r="87" fill="none" stroke="currentColor" stroke-width="6"/>
        <circle cx="320" cy="128" r="69" fill="none" stroke="currentColor" stroke-width="1.5"/>
        <path id="arc-4" d="M 242 128 A 78 78 0 0 1 398 128" fill="none"/>
        <text class="seal-arc-text"><textPath href="#arc-4" startOffset="50%" text-anchor="middle" dominant-baseline="middle">PREMIUM-QUALITÄT</textPath></text>
        <text class="seal-center" x="320" y="108" text-anchor="middle">MADE</text>
        <text class="seal-center" x="320" y="132" text-anchor="middle">IN</text>
        <text class="seal-center" x="320" y="156" text-anchor="middle">GERMANY</text>
      </g>
    </svg>
  </section>

  <!-- Gold on navy: back -->
  <section class="card card--dark card--gold" aria-label="Rückseite Gold dunkel">
    <svg viewBox="0 0 443 254" fill="currentColor">
      <rect x="53" y="50" width="338" height="148" fill="none" stroke="currentColor" stroke-width="2"/>
      <rect x="59" y="56" width="326" height="136" fill="none" stroke="currentColor" stroke-width="3"/>
      <text class="guarantee" text-anchor="middle">
        <tspan x="222" y="86">Der Gold-Feingehalt,</tspan>
        <tspan x="222" y="115">Punzierung (Stempel) auf</tspan>
        <tspan x="222" y="144">dem Schmuckstück, wird</tspan>
        <tspan x="222" y="173">hiermit garantiert</tspan>
      </text>
    </svg>
  </section>

</main>
</body>
</html>
```